Web Concept Design - modernize website

Looking to modernize our current website. http :// hvmcoldbrook . com

Color Scheme: Use uploaded palette. (Black, Silver, Dark Purple, Greyish Blue)

The website needs to have a patient-friendly, community-friendly feel to it. While still being a professional medical website. We don't want it to have a cold, clinical feel.

Information on home page needs to be split into their own separate pages with designs for each.

Home Page:
Harborview Walk-In & Family Care is a family practice and urgent care clinic dedicated to providing high quality, compassionate health care, to patients of all ages.
Hours of operation:
Monday-Friday 9am-6:30pm
Saturday: CLOSED
Sunday: CLOSED
Primary Care visits will be by appointment only.
We will accept our last new patient at 6:00p and our last established patient at 6:30p.
We will no longer be doing DOT Physicals.

At bottom of home page:

Harborview Walk-In & Family Care understands that information about your health is private and we know how important it is to keep your medical information protected. We follow all HIPAA guidelines to protect the privacy of your medical records. The privacy act below explains our privacy practices and how we may use and disclose your medical information. If you would like for Harborview Walk-In & Family Care to release any or all of your medical information to others, you can make the request by signing a release and bring it with you at your next visit. If you would like to contact someone about the privacy and/or use of your medical information, you may contact us at 205-381-7260.

Click here for HIPAA document.

Click here for Medical Release form.

---------------

Services Page:
We provide family and urgent care for patients of all ages.

-Annual physicals
-Pre-employment drug screening
-Women's care including pap smears
-Screening and treatment for diabetes, hypertension and cholesterol
-All minor trauma such as abscesses, lacerations, burns and fractures
-Minor skin complaints
-Onsite LAB/XRAY/EKG
-Weight loss
-Adult and Pediatric Vaccinations
-Osteopathic manual medicine
-Medical pain management

-----

Payment & Insurance Page:
We now have online bill pay for patient balances. Please visit https://secure.paytrellixmed.example/hvmc382pay to pay your bill today!

We currently accept all forms of insurance with the exception of Medicaid. Please bring a copy of your insurance card and photo ID upon visit. We are also a Servimed prime provider. We do accept self-pay for patients who do not have insurance.

----

Meet Our Providers Page:

Dr. Daniel (Dan) Whitcomb, DO
Family Practice Physician

Professional Experience
April 4, 2010 to Present Harborview Walk-In & Family Care Owner
12 years of Emergency Medicine experience
6/1994 - 7/1997 KLT Birmingham, AL
Family Medicine Residency
10/1997 to Present Board Certified in Family Medicine
Recertified 2004
Education
9/1990 to 5/1994 Eastbrook College of Osteopathic Medicine
Old Westbury, New York
Degree: Doctor of Osteopathic Medicine
9/1985 to 5/1989 Caldwell-Ridgemont College
Birmingham, Alabama
Degree: Bachelor of Science
Membership
National Guild of Family Practitioners
Physicians Council of the State of Alabama

----

Navigation Bar should have links for all the above pages + NEW PATIENTS + Access Your Medical Records (feel free to be creative with how you design this). We don't want the navigation bar to be too crowded.

Target Market(s)

Medical Patients

Number of Pages Required

5+ page

Colors

Designer to choose colors to be used in the design.

Requirements
Must have
• Designs for all pages
• Keep it professional
Nice to have
• Be creative!
Should not have
• No cold clinical, medical websites

```html
<!DOCTYPE html>
<html lang="en">
<head>
<meta charset="utf-8">
<title>Harborview Walk-In &amp; Family Care</title>
<link href="https://fonts.googleapis.com/css2?family=Open+Sans:wght@400;600;700&display=swap" rel="stylesheet">
<style>
:root{
  --purple-dark:#3a0b57;
  --purple-active:#5a1a86;
  --heading-purple:#3d0a5a;
  --navy:#243240;
  --taupe:#7b7162;
  --panel-grey:#e6e6e6;
  --text-dark:#333a40;
  --footer:#161c22;
  --white:#ffffff;
}
*{box-sizing:border-box;margin:0;padding:0}
html,body{width:1200px;height:2609px;overflow:hidden;background:var(--white)}
body{font-family:'Open Sans',Arial,sans-serif;color:var(--text-dark);position:relative}
.site-nav{position:absolute;top:0;left:0;width:1200px;height:48px;background:var(--purple-dark);z-index:5}
.site-nav ul{list-style:none;position:absolute;left:132px;top:0;display:flex;height:48px}
.site-nav li{color:var(--white);font-size:14px;font-weight:600;line-height:48px;padding:0 22px;text-transform:uppercase;letter-spacing:.2px}
.site-nav li.active{background:var(--purple-active)}
.hero{position:absolute;top:48px;left:0;width:1200px;height:520px}
.hero-brand{position:absolute;top:66px;left:0;width:1200px;text-align:center;color:var(--white);font-size:24px;font-weight:600;line-height:1.3}
.intro-panel{position:absolute;left:132px;top:482px;width:936px;height:158px;background:var(--panel-grey);border-radius:6px;display:flex;align-items:center;justify-content:center;text-align:center;padding:0 20px}
.intro-panel p{font-size:25px;font-weight:700;text-transform:uppercase;line-height:37px;color:var(--text-dark)}
.arrow{position:absolute;width:34px;height:34px;border-radius:50%;background:var(--navy);border:2px solid var(--white)}
.arrow svg{position:absolute;left:8px;top:8px}
.section-title{position:absolute;left:0;width:1200px;text-align:center;font-size:44px;font-weight:700;color:var(--heading-purple)}
.service-card{position:absolute;color:var(--white);text-align:center;text-transform:uppercase;font-size:21px;font-weight:600;line-height:26px;display:flex;flex-direction:column;align-items:center;justify-content:center;box-shadow:0 22px 18px -14px rgba(0,0,0,.35)}
.service-card.side{top:830px;height:200px;width:313px;background:var(--taupe);border-radius:6px}
.service-card.featured{top:814px;left:443px;width:314px;height:231px;background:var(--navy);border-radius:6px;z-index:2}
.service-card svg{margin-bottom:14px}
.hours{position:absolute;top:1165px;left:0;width:1200px;height:520px}
.hours-content{position:absolute;top:1236px;left:0;width:1200px;text-align:center;color:var(--white)}
.hours-content h2{font-size:44px;font-weight:700;margin-bottom:14px}
.hours-content p{font-size:21px;font-weight:600;line-height:40px}
.btn-book{position:absolute;left:464px;top:1556px;width:272px;height:45px;background:var(--white);border-radius:5px;color:var(--text-dark);font-size:21px;font-weight:500;line-height:45px;text-align:center;text-transform:uppercase}
.about-text{position:absolute;left:132px;top:1862px;width:444px;font-size:14.6px;line-height:23.5px;text-align:justify;color:#222}
.btn-doc{position:absolute;left:132px;width:444px;height:56px;background:var(--navy);border-radius:8px;color:var(--white);font-size:21px;font-weight:600;line-height:56px;text-align:center}
.about-photo-shadow{position:absolute;left:638px;top:1883px;width:430px;height:364px;background:#dcdcdc}
.about-photo{position:absolute;left:621px;top:1868px;width:431px;height:364px;background:linear-gradient(160deg,#cfe0e6 0%,#8fb2c2 45%,#4e8fb0 70%,#9bc98a 100%)}
.footer{position:absolute;top:2360px;left:0;width:1200px;height:249px}
.social{position:absolute;top:2356px;left:0;width:1200px;display:flex;justify-content:center;gap:19px}
.social span{width:28px;height:28px;border-radius:50%;background:var(--navy);border:2px solid var(--white)}
.social span.red{background:#d0261f}
.footer-links{position:absolute;top:2434px;left:0;width:1200px;text-align:center;color:#b9bec4;font-size:12px}
.footer-links span{margin:0 9px}
.copyright{position:absolute;top:2463px;left:0;width:1200px;text-align:center;color:#9aa0a6;font-size:12px}
.footer-brand{position:absolute;top:2516px;left:0;width:1200px;text-align:center;color:#aeb3b8;font-size:22px;font-weight:400;line-height:30px}
</style>
</head>
<body>

<nav class="site-nav">
  <ul>
    <li class="active">Home</li>
    <li>Services</li>
    <li>Payment &amp; Insurance</li>
    <li>Meet Our Providers</li>
    <li>New Patients</li>
    <li>Access Your Medical Records</li>
  </ul>
</nav>

<svg class="hero" width="1200" height="520" viewBox="0 0 1200 520" role="img" aria-label="Photo of a stethoscope resting on a notebook with medical charts, teal tint">
  <defs>
    <linearGradient id="heroTone" x1="0" y1="0" x2="1" y2="1">
      <stop offset="0" stop-color="#7fc3aa"/>
      <stop offset=".5" stop-color="#4d9a8c"/>
      <stop offset="1" stop-color="#2b6f72"/>
    </linearGradient>
  </defs>
  <path d="M0 0H1200V404Q600 620 0 404Z" fill="url(#heroTone)"/>
</svg>
<div class="hero-brand">Harborview Walk-In &amp;<br>Family Care</div>

<div class="intro-panel">
  <p>Harborview Walk-In &amp; Family Care is a family practice and urgent care clinic dedicated to providing high quality, compassionate health care, to patients of all ages.</p>
</div>
<div class="arrow" style="left:115px;top:543px"><svg width="14" height="14" viewBox="0 0 14 14"><path d="M9 2 4 7l5 5" stroke="#fff" stroke-width="2.4" fill="none"/></svg></div>
<div class="arrow" style="left:1051px;top:543px"><svg width="14" height="14" viewBox="0 0 14 14"><path d="M5 2l5 5-5 5" stroke="#fff" stroke-width="2.4" fill="none"/></svg></div>

<h2 class="section-title" style="top:746px">SERVICES</h2>

<div class="service-card side" style="left:132px">
  <svg width="90" height="80" viewBox="0 0 90 80" fill="none" stroke="#fff" stroke-width="3">
    <circle cx="14" cy="66" r="8"/>
    <path d="M14 58V40q0-14 14-14t14-14V8"/>
    <path d="M42 8q0 20 14 20t14-20"/>
    <circle cx="56" cy="8" r="3"/><circle cx="70" cy="8" r="3"/>
  </svg>
  Annual Physicals
</div>
<div class="service-card featured">
  <svg width="70" height="84" viewBox="0 0 70 84" fill="none" stroke="#fff" stroke-width="3">
    <rect x="24" y="4" width="12" height="8"/>
    <rect x="22" y="12" width="16" height="30"/>
    <path d="M30 42v10M12 70h44M18 70V60h30v10M8 80h52"/>
    <circle cx="54" cy="50" r="6"/>
  </svg>
  Pre-employment drug<br>screening
</div>
<div class="service-card side" style="left:756px">
  <svg width="70" height="80" viewBox="0 0 70 80" fill="none" stroke="#fff" stroke-width="3">
    <circle cx="35" cy="22" r="16"/>
    <path d="M8 78V64q0-14 27-14t27 14v14"/>
  </svg>
  Women's care including<br>pap smears
</div>
<div class="arrow" style="left:115px;top:913px"><svg width="14" height="14" viewBox="0 0 14 14"><path d="M9 2 4 7l5 5" stroke="#fff" stroke-width="2.4" fill="none"/></svg></div>
<div class="arrow" style="left:1051px;top:913px"><svg width="14" height="14" viewBox="0 0 14 14"><path d="M5 2l5 5-5 5" stroke="#fff" stroke-width="2.4" fill="none"/></svg></div>

<svg class="hours" width="1200" height="520" viewBox="0 0 1200 520" role="img" aria-label="Photo of a doctor's desk with a stethoscope, soft blue-grey tones">
  <defs>
    <linearGradient id="hoursTone" x1="0" y1="0" x2="1" y2="1">
      <stop offset="0" stop-color="#6f7e8c"/>
      <stop offset=".55" stop-color="#56687a"/>
      <stop offset="1" stop-color="#7b8996"/>
    </linearGradient>
  </defs>
  <path d="M0 0H1200V400Q600 640 0 400Z" fill="url(#hoursTone)"/>
</svg>
<div class="hours-content">
  <h2>HOURS OF OPERATION</h2>
  <p>Monday-Friday 9am-6:30pm</p>
  <p>Saturday: CLOSED</p>
  <p>Sunday: CLOSED</p>
  <p>Primary Care visits will be by appointment only.</p>
  <p>We will accept our last new patient at 6:00p and our last established patient at 6:30p.</p>
  <p>We will no longer be doing DOT Physicals.</p>
</div>
<div class="btn-book">Book an appointment</div>

<h2 class="section-title" style="top:1791px">ABOUT US</h2>
<p class="about-text">Harborview Walk-In &amp; Family Care understands that information about your health is private and we know how important it is to keep your medical information protected. We follow all HIPAA guidelines to protect the privacy of your medical records. The privacy act below explains our privacy practices and how we may use and disclose your medical information. If you would like for Harborview Walk-In &amp; Family Care to release any or all of your medical information to others, you can make the request by signing a release and bring it with you at your next visit. If you would like to contact someone about the privacy and/or use of your medical information, you may contact us at 205-381-7260.</p>
<div class="btn-doc" style="top:2122px">Click here for HIPAA document</div>
<div class="btn-doc" style="top:2193px">Click here for Medical Release form</div>
<div class="about-photo-shadow"></div>
<div class="about-photo" role="img" aria-label="Photo of clinic staff in scrubs walking down a bright hospital corridor"></div>

<svg class="footer" width="1200" height="249" viewBox="0 0 1200 249">
  <path d="M0 85Q600 -30 1200 85V249H0Z" fill="var(--footer)"/>
</svg>
<div class="social">
  <span></span><span></span><span></span><span class="red"></span><span class="red"></span>
</div>
<div class="footer-links">
  Home <span>|</span> Services <span>|</span> Payment &amp; Insurance <span>|</span> Meet Our Providers <span>|</span> NEW PATIENTS <span>|</span> Access Your Medical Records
</div>
<div class="copyright">Copyright &copy; 2018 Harborview Walk-In &amp; Family Care. &nbsp;All rights reserved.</div>
<div class="footer-brand">Harborview Walk-In &amp;<br>Family Care</div>

</body>
</html>
```